Business Card Design

We require a business card design for a law firm, our signature colours are maroon and cream. Our slogan is "From our family to yours", we would like the cards to be professional however feminine at the same time.

Industry/Entity Type

Business

Contact Information for Business Card

Helena Brackett & Associates Lawyers & Conveyancers, Helena Brackett LL.B. Principal Solicitor, 17 Quillon Street, Marrowdale NSW 2190

Logo styles of interest
Emblem Logo
Abstract Logo
Wordmark Logo

```html
<!DOCTYPE html>
<html lang="en">
<head>
<meta charset="utf-8">
<title>Helena Brackett &amp; Associates — Business Card</title>
<link rel="stylesheet" href="https://fonts.googleapis.com/css2?family=Noto+Serif:wght@400&display=swap">
<style>
  :root {
    --page: #ececec;
    --maroon: #8a3459;
    --maroon-deep: #7a2b4d;
    --maroon-shade: #812f53;
    --cream: #e8c996;
    --cream-soft: #dcb98a;
  }
  * { box-sizing: border-box; margin: 0; padding: 0; }
  html, body {
    width: 1200px;
    height: 800px;
    overflow: hidden;
    background: var(--page);
  }
  .canvas {
    width: 1200px;
    height: 800px;
    display: flex;
    align-items: center;
    justify-content: center;
  }
  .business-card {
    width: 420px;
    height: 690px;
    background: var(--maroon);
    color: var(--cream);
    font-family: "Noto Serif", Georgia, serif;
    text-align: center;
    display: flex;
    flex-direction: column;
    align-items: center;
    box-shadow: 0 10px 30px rgba(0,0,0,0.12);
  }
  .brand {
    width: 100%;
    padding-top: 52px;
    display: flex;
    flex-direction: column;
    align-items: center;
  }
  .brand-dot {
    width: 84px;
    height: 84px;
    border-radius: 50%;
    background: var(--cream);
    margin-bottom: 26px;
  }
  .brand-name {
    font-size: 21px;
    line-height: 1.35;
    color: var(--cream);
  }
  .slogan-band {
    width: 100%;
    margin-top: 26px;
    padding: 16px 0;
    background: var(--maroon-deep);
    border-top: 1px solid var(--maroon-shade);
    border-bottom: 1px solid var(--maroon-shade);
    font-size: 20px;
    letter-spacing: 0.5px;
    text-transform: uppercase;
  }
  .firm-details {
    margin-top: 40px;
    font-size: 20px;
    line-height: 1.3;
  }
  .divider-flourish {
    width: 150px;
    height: 40px;
    margin-top: 38px;
    border-radius: 20px;
    background: linear-gradient(90deg, transparent, var(--cream-soft) 30%, var(--cream-soft) 70%, transparent);
    opacity: 0.55;
  }
  .address {
    margin-top: 48px;
    font-size: 20px;
    line-height: 1.3;
  }
</style>
</head>
<body>
  <main class="canvas">
    <article class="business-card">
      <header class="brand">
        <span class="brand-dot" aria-hidden="true"></span>
        <p class="brand-name">Helena Brackett &amp; Associates<br>Lawyers</p>
      </header>
      <p class="slogan-band">From our family to yours</p>
      <p class="firm-details">
        Helena Brackett &amp; Associates<br>
        Lawyers &amp; Conveyancers,<br>
        Helena Brackett LL.B.
      </p>
      <div class="divider-flourish" role="img" aria-label="Decorative scroll flourish divider"></div>
      <address class="address" style="font-style: normal;">
        Principal Solicitor,<br>
        17 Quillon Street,<br>
        Marrowdale NSW 2190
      </address>
    </article>
  </main>
</body>
</html>
```